Survey App for phone users trying a new phone with Dual connectivity

Survey App Brief<br/>Design For an Android Survey App for users' feedback on Call, SMS, Data and Streaming Experience on their Mobile phones.<br/><br/>Purpose of the App<br/>To ensure that the user's experience is not impacted by the network switching between two network on the special mobile phones they newly started using.<br/><br/>App Requirements:<br/>First screen: The registration screen, where the user needs to enter the following:<br/>Name: text box<br/>Phone Number: text box<br/>Group Number : <br/><br/>An information text:<br/>By Registering I agree to participate in the Survey.<br/><br/>Register: Button<br/><br/>Start Screen - Survey screens (next time user open the App this will be the first screen):<br/>We need feedback for 4 indicators:<br/>Call Experience<br/>SMS Experience<br/>Data Experience<br/>Streaming Experience<br/><br/>Each Experience can be in the form of a questionnaire or Satisfied/ Somewhat Satisfied / Extremely Satisfied form with radio buttons or on a scale of 1 to 5. We need to ensure that the format used is very professional.<br/><br/>An optional text box for the user to enter the comment in a free format.<br/><br/>This can be done in 4 different screens or in one single screen if it does not give a clumsy look.<br/><br/>A Send button at the end to submit the Survey.<br/><br/>We need a burger menu at the top left corner of this screen, which when expanded will provide 5 options:<br/>Edit User Profile<br/>Survey interval Timer<br/>FAQ<br/>Exit<br/>About<br/><br/><br/>Please ensure that the app is simple, friendly, lively and professional at the same time so that it ignites an interest in the user to use the app.<br/>Use Logo as appropriate.
Telecommunications
Colors
Designer to choose colors to be used in the design.

```html
<!DOCTYPE html>
<html lang="en">
<head>
<meta charset="utf-8">
<title>Survey App</title>
<link href="https://fonts.googleapis.com/css2?family=Roboto:wght@300;400;500;700&display=swap" rel="stylesheet">
<style>
:root{
  --bg:#cfcfcf;
  --navy:#0d4aa6;
  --btn:#0b47a3;
  --sky:#4fb0f0;
  --sky-light:#84d0f6;
  --white:#ffffff;
  --ink:#111111;
  --muted:#777777;
  --field:#ececec;
  --back:#555555;
  --dim:#7a7a7a;
  --dim-panel:#3b607f;
  --dim-btn:#2c4b74;
}
*{box-sizing:border-box;margin:0;padding:0}
html,body{width:1099px;height:1200px;overflow:hidden;background:var(--bg)}
body{position:relative;font-family:'Roboto',sans-serif;color:var(--ink)}
.page-title{position:absolute;left:0;width:1106px;top:52px;text-align:center;font-size:37px;font-weight:700;color:var(--navy);letter-spacing:.5px}
.screen-label{position:absolute;width:300px;text-align:center;font-size:22px;font-weight:400;letter-spacing:.6px;color:var(--ink)}
.screen{position:absolute;width:223px;height:397px;background:var(--white);overflow:hidden}
.status{position:absolute;left:0;right:0;top:0;height:16px;font-size:9px;font-weight:500;padding:4px 0 0 6px}
.status svg{position:absolute;right:4px;top:4px}
/* brand */
.brand{position:absolute;display:flex;align-items:center;gap:8px}
.brand-dot{width:30px;height:30px;border-radius:50%;background:var(--sky-light)}
.brand-name{font-size:12px;font-weight:400;letter-spacing:1.6px;color:#8a9096}
/* registration */
.reg-panel{position:absolute;left:0;top:72px;width:223px;height:325px;background:var(--sky);border-radius:24px}
.reg-title{position:absolute;left:0;right:0;top:19px;text-align:center;color:var(--white);font-size:17px;font-weight:500}
.field{position:absolute;left:23px;width:178px;height:29px;background:var(--white);border-radius:5px;font-size:10px;color:var(--muted);padding:8px 0 0 8px}
.consent{position:absolute;left:0;right:0;top:238px;text-align:center;font-size:8px;color:var(--ink)}
.btn-register{position:absolute;left:58px;top:265px;width:107px;height:29px;background:var(--btn);border-radius:4px;color:var(--white);font-size:17px;font-weight:500;text-align:center;line-height:29px}
/* nav drawer */
.nav-screen{background:var(--dim)}
.drawer-bg{position:absolute;left:0;top:0}
.avatar{position:absolute;left:12px;top:18px;width:30px;height:30px;border-radius:50%;background:linear-gradient(#f5c9a8,#e2533f);border:2px solid var(--white)}
.user-name{position:absolute;left:57px;top:20px;font-size:14px;color:var(--white)}
.user-phone{position:absolute;left:57px;top:37px;font-size:10.5px;color:#10233a}
.nav-item{position:absolute;left:13px;display:flex;align-items:center;gap:17px;font-size:14px;font-weight:500;color:var(--white)}
.nav-icon{width:27px;height:27px;border-radius:50%;background:var(--white);display:flex;align-items:center;justify-content:center}
.dim-comments{position:absolute;left:10px;top:291px;width:205px;height:59px;background:#8a8a8a;border-radius:5px;font-size:9.5px;color:#444;padding:7px}
.dim-next{position:absolute;left:154px;top:361px;width:60px;height:24px;background:var(--dim-btn);color:#8aa0b8;font-size:14px;font-weight:500;text-align:center;line-height:24px;border-radius:2px}
/* survey */
.menu-icon{position:absolute;left:10px;top:36px;width:18px}
.menu-icon span{display:block;height:3px;border-radius:2px;background:var(--sky);margin:0 auto 4px}
.app-title{position:absolute;left:51px;top:34px;font-size:18.5px;font-weight:500;color:var(--sky);letter-spacing:.2px}
.feedback-panel{position:absolute;left:0;top:73px;width:223px;height:208px;background:var(--sky);border-radius:24px}
.panel-head{position:absolute;left:0;right:0;top:6px;text-align:center;font-size:18px;font-weight:300;color:var(--white)}
.panel-rule{position:absolute;left:0;right:0;top:33px;height:1.5px;background:#d8eefc}
.question{position:absolute;left:13px;top:43px;font-size:15.5px;font-weight:500;color:var(--white)}
.option{position:absolute;left:11px;width:202px;height:28px;background:var(--white);border-radius:6px;font-size:11px;color:var(--muted);display:flex;align-items:center;padding-left:12px;gap:13px}
.radio{width:13px;height:13px;border-radius:50%;border:1.3px solid var(--sky)}
.option.selected{color:var(--navy);font-weight:500}
.option.selected .radio{background:var(--navy);border-color:var(--navy)}
.comments{position:absolute;left:10px;top:292px;width:206px;height:59px;background:var(--field);border-radius:5px;font-size:9.5px;color:#444;padding:7px}
.btn{position:absolute;top:361px;width:60px;height:24px;color:var(--white);font-size:14px;font-weight:500;text-align:center;line-height:24px;border-radius:2px}
.btn-next{left:155px;background:var(--btn)}
.btn-back{left:11px;background:var(--back)}
.btn-submit{left:147px;width:68px;background:var(--btn);border-radius:12px}
</style>
</head>
<body>
<h1 class="page-title">SURVEY APP</h1>

<h2 class="screen-label" style="left:101px;top:152px">SPLASH SCREEN</h2>
<h2 class="screen-label" style="left:383px;top:152px">REGISTRATION</h2>
<h2 class="screen-label" style="left:674px;top:152px">NAV_BAR SCREEN</h2>

<!-- Splash -->
<section class="screen splash" style="left:139px;top:203px">
  <div class="brand" style="left:46px;top:163px"><span class="brand-dot"></span><span class="brand-name">MERIDIAN LABS</span></div>
</section>

<!-- Registration -->
<section class="screen registration" style="left:425px;top:203px">
  <div class="status">9:41<svg width="50" height="8" viewBox="0 0 50 8"><rect x="0" y="5" width="2" height="3" fill="#111"/><rect x="3" y="3" width="2" height="5" fill="#111"/><rect x="6" y="1" width="2" height="7" fill="#111"/><path d="M16 3a6 6 0 0 1 8 0M18 5a3 3 0 0 1 4 0" stroke="#111" fill="none" stroke-width="1.3"/><circle cx="20" cy="7" r="1" fill="#111"/><rect x="32" y="1" width="14" height="6" rx="1" fill="#111"/><rect x="47" y="3" width="1" height="2" fill="#111"/></svg></div>
  <div class="brand" style="left:45px;top:27px"><span class="brand-dot"></span><span class="brand-name">MERIDIAN LABS</span></div>
  <div class="reg-panel">
    <h3 class="reg-title">REGISTRATION</h3>
    <div class="field" style="top:54px">Name</div>
    <div class="field" style="top:102px">Phone Number</div>
    <div class="field" style="top:149px">Group Number</div>
    <p class="consent">By Registering I Agree To Participate In The Survey.</p>
    <div class="btn-register">REGISTER</div>
  </div>
</section>

<!-- Nav drawer -->
<section class="screen nav-screen" style="left:713px;top:203px">
  <svg class="drawer-bg" width="223" height="397" viewBox="0 0 223 397">
    <defs><linearGradient id="drawerGrad" x1="1" y1="0" x2="0" y2="1"><stop offset="0" stop-color="#86d3f6"/><stop offset="1" stop-color="#3fa2ee"/></linearGradient></defs>
    <rect x="0" y="0" width="223" height="282" rx="24" fill="var(--dim-panel)"/>
    <rect x="0" y="0" width="223" height="30" fill="var(--dim-panel)"/>
    <rect x="11" y="190" width="200" height="29" rx="5" fill="#6f8697"/>
    <rect x="11" y="232" width="200" height="29" rx="5" fill="#6f8697"/>
    <path d="M0 0H223V140C223 200 170 253 95 253H0Z" fill="url(#drawerGrad)"/>
  </svg>
  <div class="avatar" role="img" aria-label="User profile photo"></div>
  <div class="user-name">Name</div>
  <div class="user-phone">Phone Number</div>
  <div class="nav-item" style="top:69px"><span class="nav-icon"><svg width="14" height="14" viewBox="0 0 14 14" fill="none" stroke="#3fa2ee" stroke-width="1.2"><circle cx="7" cy="4.5" r="3"/><path d="M1.5 13c0-3 2.5-5 5.5-5s5.5 2 5.5 5"/></svg></span>Edit User Profile</div>
  <div class="nav-item" style="top:101px"><span class="nav-icon"><svg width="14" height="14" viewBox="0 0 14 14" fill="none" stroke="#3fa2ee" stroke-width="1.2"><rect x="2.5" y="1.5" width="9" height="11" rx="1"/><path d="M4.5 5h5M4.5 7.5h5M4.5 10h5"/></svg></span>Survey Interval Timer</div>
  <div class="nav-item" style="top:133px"><span class="nav-icon"><svg width="14" height="14" viewBox="0 0 14 14" fill="none" stroke="#3fa2ee" stroke-width="1.2"><path d="M1.5 3h8v6h-5l-3 2.5z"/><circle cx="10" cy="4" r="3"/></svg></span>FAQ</div>
  <div class="nav-item" style="top:165px"><span class="nav-icon"><svg width="14" height="14" viewBox="0 0 14 14" fill="none" stroke="#3fa2ee" stroke-width="1.2"><rect x="7" y="1.5" width="5.5" height="11"/><path d="M1.5 7h7M6 4.5 8.5 7 6 9.5"/></svg></span>Exit</div>
  <div class="nav-item" style="top:197px"><span class="nav-icon"><svg width="14" height="14" viewBox="0 0 14 14" fill="none" stroke="#3fa2ee" stroke-width="1.2"><circle cx="7" cy="7" r="5.5"/><path d="M7 6v4.2"/><circle cx="7" cy="4" r=".6" fill="#3fa2ee"/></svg></span>About</div>
  <div class="dim-comments">Comments</div>
  <div class="dim-next">Next</div>
</section>

<h2 class="screen-label" style="left:-8px;top:671px">CALL EXPERIENCE</h2>
<h2 class="screen-label" style="left:261px;top:671px">SMS EXPERIENCE</h2>
<h2 class="screen-label" style="left:532px;top:671px">DATA EXPERIENCE</h2>
<h2 class="screen-label" style="left:807px;top:671px;width:300px">STREAMING EXPERIENCE</h2>

<!-- Survey 1 -->
<section class="screen survey" style="left:32px;top:733px">
  <div class="status">9:41<svg width="50" height="8" viewBox="0 0 50 8"><rect x="0" y="5" width="2" height="3" fill="#111"/><rect x="3" y="3" width="2" height="5" fill="#111"/><rect x="6" y="1" width="2" height="7" fill="#111"/><path d="M16 3a6 6 0 0 1 8 0M18 5a3 3 0 0 1 4 0" stroke="#111" fill="none" stroke-width="1.3"/><circle cx="20" cy="7" r="1" fill="#111"/><rect x="32" y="1" width="14" height="6" rx="1" fill="#111"/><rect x="47" y="3" width="1" height="2" fill="#111"/></svg></div>
  <div class="menu-icon"><span style="width:12px"></span><span style="width:18px"></span><span style="width:12px"></span></div>
  <h3 class="app-title">QUICK SURVEY</h3>
  <div class="feedback-panel">
    <div class="panel-head">Feedback</div><div class="panel-rule"></div>
    <h4 class="question">1. Call Experience</h4>
    <div class="option" style="top:72px"><span class="radio"></span>Questionnaire or Satisfied</div>
    <div class="option" style="top:116px"><span class="radio"></span>Somewhat Satisfied</div>
    <div class="option selected" style="top:160px"><span class="radio"></span>Extremely Satisfied</div>
  </div>
  <div class="comments">Comments</div>
  <div class="btn btn-next">Next</div>
</section>

<!-- Survey 2 -->
<section class="screen survey" style="left:299px;top:733px">
  <div class="status">9:41<svg width="50" height="8" viewBox="0 0 50 8"><rect x="0" y="5" width="2" height="3" fill="#111"/><rect x="3" y="3" width="2" height="5" fill="#111"/><rect x="6" y="1" width="2" height="7" fill="#111"/><path d="M16 3a6 6 0 0 1 8 0M18 5a3 3 0 0 1 4 0" stroke="#111" fill="none" stroke-width="1.3"/><circle cx="20" cy="7" r="1" fill="#111"/><rect x="32" y="1" width="14" height="6" rx="1" fill="#111"/><rect x="47" y="3" width="1" height="2" fill="#111"/></svg></div>
  <div class="menu-icon"><span style="width:12px"></span><span style="width:18px"></span><span style="width:12px"></span></div>
  <h3 class="app-title">QUICK SURVEY</h3>
  <div class="feedback-panel">
    <div class="panel-head">Feedback</div><div class="panel-rule"></div>
    <h4 class="question">2. SMS Experience</h4>
    <div class="option" style="top:72px"><span class="radio"></span>Questionnaire or Satisfied</div>
    <div class="option" style="top:116px"><span class="radio"></span>Somewhat Satisfied</div>
    <div class="option selected" style="top:160px"><span class="radio"></span>Extremely Satisfied</div>
  </div>
  <div class="comments">Comments</div>
  <div class="btn btn-back">Back</div>
  <div class="btn btn-next">Next</div>
</section>

<!-- Survey 3 -->
<section class="screen survey" style="left:568px;top:733px">
  <div class="status">9:41<svg width="50" height="8" viewBox="0 0 50 8"><rect x="0" y="5" width="2" height="3" fill="#111"/><rect x="3" y="3" width="2" height="5" fill="#111"/><rect x="6" y="1" width="2" height="7" fill="#111"/><path d="M16 3a6 6 0 0 1 8 0M18 5a3 3 0 0 1 4 0" stroke="#111" fill="none" stroke-width="1.3"/><circle cx="20" cy="7" r="1" fill="#111"/><rect x="32" y="1" width="14" height="6" rx="1" fill="#111"/><rect x="47" y="3" width="1" height="2" fill="#111"/></svg></div>
  <div class="menu-icon"><span style="width:12px"></span><span style="width:18px"></span><span style="width:12px"></span></div>
  <h3 class="app-title">QUICK SURVEY</h3>
  <div class="feedback-panel">
    <div class="panel-head">Feedback</div><div class="panel-rule"></div>
    <h4 class="question">3. Data Experience</h4>
    <div class="option" style="top:72px"><span class="radio"></span>Questionnaire or Satisfied</div>
    <div class="option selected" style="top:116px"><span class="radio"></span>Somewhat Satisfied</div>
    <div class="option" style="top:160px"><span class="radio"></span>Extremely Satisfied</div>
  </div>
  <div class="comments">Data Connectivity Is Bit Slow.</div>
  <div class="btn btn-back">Back</div>
  <div class="btn btn-next">Next</div>
</section>

<!-- Survey 4 -->
<section class="screen survey" style="left:841px;top:733px">
  <div class="status">9:41<svg width="50" height="8" viewBox="0 0 50 8"><rect x="0" y="5" width="2" height="3" fill="#111"/><rect x="3" y="3" width="2" height="5" fill="#111"/><rect x="6" y="1" width="2" height="7" fill="#111"/><path d="M16 3a6 6 0 0 1 8 0M18 5a3 3 0 0 1 4 0" stroke="#111" fill="none" stroke-width="1.3"/><circle cx="20" cy="7" r="1" fill="#111"/><rect x="32" y="1" width="14" height="6" rx="1" fill="#111"/><rect x="47" y="3" width="1" height="2" fill="#111"/></svg></div>
  <div class="menu-icon"><span style="width:12px"></span><span style="width:18px"></span><span style="width:12px"></span></div>
  <h3 class="app-title">QUICK SURVEY</h3>
  <div class="feedback-panel">
    <div class="panel-head">Feedback</div><div class="panel-rule"></div>
    <h4 class="question">4. Streaming Experience</h4>
    <div class="option selected" style="top:72px"><span class="radio"></span>Questionnaire or Satisfied</div>
    <div class="option" style="top:116px"><span class="radio"></span>Somewhat Satisfied</div>
    <div class="option" style="top:160px"><span class="radio"></span>Extremely Satisfied</div>
  </div>
  <div class="comments">Comments</div>
  <div class="btn btn-back">Back</div>
  <div class="btn btn-submit">SUBMIT</div>
</section>
</body>
</html>
```